Business Card Design for skin care range

The skincare range created here is a revolutionized skin care range that is very unique, natural and great for all skin types.The skincare range is cooled in nature, organic and rejuvenating for all skin types. 'Glow Fern Bright' aims to radiate the vibe of wellness and harmony throughout our skin. The products are developed via bio-pharmaceutical high grade processes to put the life and radiance back in our skin.

Target Market(s)

All ages, as the skincare is great for all skin types.

Industry/Entity Type

Business

Contact Information for Business Card

M: 04 586 731 92 E: hello@dewpalora.com S: www.dewpalora.com

Font styles to use
Serif
Sans Serif
Script

Colors
0692cd

Requirements
Must have
• The business card we are aiming for is a simple yet elegant appeal with a black and white picture set in the middle of the business card (landscape orientation) with the caption "Glow Fern Bright" centered spanning across the whole card horizontally. We are thinking having coloured (light-ish/ aqua coloured blue). we want the image encapsulated within a prestige/ mirror frame kind of border that is simply shown through the cutting out of the image. The remaining space on the card shall have a white background with a misty tonal fog that sweeps across the white.On the back of the card will be the text "Glow Fern Bright" in the color blue being the hierarchical text. (same as the 'me' on the front).All other relevant contact information is in black. with also the statement "Keep me chilled" (as the products are to be refrigerated) in a different style so it is unique from the rest as its an important note. Also under the glow fern bright text, i'd like to have the text "Bio-organic pharmaceutical grade skincare range" added to the card to emphasis the quality and uniqueness of the product. For the back of the card's background, the hazy tonal fog shall span across the whole backside of the card with the white background, keeping it plain and simple.
Nice to have
• Weare aiming for a professional elegant and classy look, with also that natural and joyful appeal.
• A black and white close up picture of a young persons face (preferably a girls face) to create the appeal of youth. The eyes must be of high importance. see the pictures we've uploaded and trial with them as we love the pictures of the girls faces

```html
<!DOCTYPE html>
<html lang="en">
<head>
<meta charset="utf-8">
<title>Glow Fern Bright – Business Card</title>
<link href="https://fonts.googleapis.com/css2?family=Cinzel:wght@400&family=Raleway:wght@300&display=swap" rel="stylesheet">
<style>
  :root {
    --stage: #454545;
    --card: #f2f2f2;
    --fog-light: #fafafa;
    --fog-mid: #e2e2e2;
    --frame: #a9a9a9;
    --ornament: #d4d4d4;
    --brand-blue: #0692cd;
    --ink: #555555;
    --ink-soft: #7a7a7a;
  }
  html, body {
    margin: 0;
    width: 1200px;
    height: 1000px;
    overflow: hidden;
    background: var(--stage);
  }
  .stage { position: relative; width: 1200px; height: 1000px; }
  .card {
    position: absolute;
    left: 253px;
    width: 694px;
    height: 406px;
    overflow: hidden;
    background: var(--card);
  }
  .card--front { top: 63px; }
  .card--back { top: 530px; }
  .fog {
    position: absolute; inset: 0;
    background:
      radial-gradient(ellipse 60% 40% at 25% 70%, var(--fog-light), transparent 70%),
      radial-gradient(ellipse 50% 35% at 75% 30%, var(--fog-light), transparent 70%),
      linear-gradient(180deg, var(--fog-mid), var(--card) 60%, var(--fog-mid));
  }
  .portrait {
    position: absolute;
    left: 100px; top: 0;
    width: 494px; height: 300px;
    background: radial-gradient(ellipse 55% 75% at 50% 40%, #cfcfcf, #b8b8b8 45%, rgba(236,236,236,0) 100%);
  }
  .frame { position: absolute; inset: 0; }
  .ornament {
    position: absolute;
    width: 58px; height: 58px;
    background: var(--ornament);
    border-radius: 6px;
  }
  .ornament--tl { left: 12px; top: 6px; }
  .ornament--tr { right: 12px; top: 6px; }
  .ornament--bl { left: 12px; bottom: 6px; }
  .ornament--br { right: 12px; bottom: 6px; }
  .brand-name {
    position: absolute;
    left: 0; right: 0;
    margin: 0;
    text-align: center;
    font-family: "Cinzel", serif;
    font-weight: 400;
    font-size: 50px;
    color: var(--brand-blue);
    letter-spacing: 1px;
  }
  .card--front .brand-name { top: 310px; }
  .card--back .brand-name { top: 70px; }
  .range-line {
    position: absolute; left: 0; right: 0; top: 164px;
    margin: 0; text-align: center;
    font-family: "Raleway", sans-serif; font-weight: 300;
    font-size: 19px; color: var(--ink-soft);
  }
  .chill-note {
    position: absolute; left: 0; right: 0; top: 204px;
    margin: 0; text-align: center;
    font-family: "Cinzel", serif; font-size: 28px; color: var(--ink);
  }
  .chill-note .accent { color: var(--brand-blue); }
  .contact {
    position: absolute; left: 0; right: 0; top: 272px;
    margin: 0; padding: 0; list-style: none; text-align: center;
    font-family: "Raleway", sans-serif; font-weight: 300;
    font-size: 24px; line-height: 34px; color: var(--ink);
  }
  .contact .label { font-family: "Cinzel", serif; color: var(--brand-blue); }
</style>
</head>
<body>
<div class="stage">

  <section class="card card--front">
    <div class="fog"></div>
    <div class="portrait" role="img" aria-label="Black and white close-up portrait of a young girl, fading into mist"></div>
    <svg class="frame" width="694" height="406" viewBox="0 0 694 406" aria-hidden="true">
      <g fill="none" stroke="var(--frame)" stroke-width="1.5">
        <line x1="12" y1="75" x2="12" y2="330"/>
        <line x1="682" y1="75" x2="682" y2="330"/>
        <line x1="80" y1="395" x2="614" y2="395"/>
      </g>
    </svg>
    <div class="ornament ornament--tl" role="img" aria-label="Filigree corner ornament"></div>
    <div class="ornament ornament--tr" role="img" aria-label="Filigree corner ornament"></div>
    <div class="ornament ornament--bl" role="img" aria-label="Filigree corner ornament"></div>
    <div class="ornament ornament--br" role="img" aria-label="Filigree corner ornament"></div>
    <h1 class="brand-name">Glow Fern Bright</h1>
  </section>

  <section class="card card--back">
    <div class="fog"></div>
    <svg class="frame" width="694" height="406" viewBox="0 0 694 406" aria-hidden="true">
      <g fill="none" stroke="var(--frame)" stroke-width="1.5">
        <line x1="80" y1="11" x2="614" y2="11"/>
        <line x1="80" y1="395" x2="614" y2="395"/>
        <line x1="12" y1="75" x2="12" y2="330"/>
        <line x1="682" y1="75" x2="682" y2="330"/>
      </g>
    </svg>
    <div class="ornament ornament--tl" role="img" aria-label="Filigree corner ornament"></div>
    <div class="ornament ornament--tr" role="img" aria-label="Filigree corner ornament"></div>
    <div class="ornament ornament--bl" role="img" aria-label="Filigree corner ornament"></div>
    <div class="ornament ornament--br" role="img" aria-label="Filigree corner ornament"></div>
    <h2 class="brand-name">Glow Fern Bright</h2>
    <p class="range-line">Bio-organic Pharmaceutical Grade Skincare Range.</p>
    <p class="chill-note">KEEP ME <span class="accent">CHILLED.</span></p>
    <ul class="contact">
      <li><span class="label">M:</span> 04 586 731 92</li>
      <li><span class="label">E:</span> hello@dewpalora.com</li>
      <li><span class="label">S:</span> www.dewpalora.com</li>
    </ul>
  </section>

</div>
</body>
</html>
```